Business Card - Professional Minimalist - Double sided

We appreciate minimalist logo/web/collateral designs that allow design to tell a story. We want to relay a professional image/approach but throwing in a splash of modern when we’re able so long as it’s not distracting. Think 75% classic corporate, 25% modern. Open to black or white design, not sure which might look the best.

Target Market(s)

Senior executives or related government affairs contacts within the agriculture, energy, and defense industries (i.e., potential clients) but located outside of Washington, DC. Most potential clients based in DC with be familiar with both of us and our shared history.

Industry/Entity Type

Consulting

Contact Information for Business Card

Name: Daniel R. Whitlock
Title: Co-Founder & Partner
Address: 418 Bramblewood Ave. SE | Suite 2716 | Washington, D.C. 20019
Phone: (202) 555-0187
Email: Daniel@HollerbyWhitlock.com

Font styles to use
Serif

Colors

Designer to choose only greyscale colors for use in the design.

Requirements
Must have
• Name: Daniel R. Whitlock
Phone: (202) 555-0187

```html
<!DOCTYPE html>
<html lang="en">
<head>
<meta charset="utf-8">
<title>Hollerby Whitlock Group – Business Card</title>
<link href="https://fonts.googleapis.com/css2?family=Arimo:wght@400;700&display=swap" rel="stylesheet">
<style>
  :root {
    --canvas: #e9e9e9;
    --card-light: #f6f6f6;
    --card-dark: #5a5a5a;
    --ink: #4e4e4e;
    --ink-soft: #6a6a6a;
    --rule: #9a9a9a;
    --mark-light: #d8d8d8;
  }
  * { box-sizing: border-box; margin: 0; padding: 0; }
  html, body {
    width: 1200px; height: 967px; overflow: hidden;
    background: var(--canvas);
    font-family: "Arimo", Arial, sans-serif;
  }
  .sheet {
    position: relative; width: 1200px; height: 967px;
    display: flex; align-items: center; justify-content: center; gap: 40px;
  }
  .card {
    position: relative; width: 555px; height: 317px;
    box-shadow: 0 2px 6px rgba(0,0,0,0.12);
  }
  .card--front { background: var(--card-light); color: var(--ink); padding: 26px 30px; }
  .card--back { background: var(--card-dark); display: flex; align-items: center; justify-content: center; }

  .wordmark { display: flex; align-items: center; gap: 10px; }
  .wordmark__square { width: 24px; height: 24px; background: var(--ink-soft); }
  .wordmark__name {
    font-size: 15px; font-weight: 400; letter-spacing: 0.14em;
    text-transform: uppercase; color: var(--ink);
  }
  .wordmark-rule { margin: 10px 0 0 34px; width: 270px; height: 1px; background: var(--rule); }

  .person { margin-top: 26px; }
  .person__name { font-size: 25px; font-weight: 700; color: var(--ink); }
  .person__title { margin-top: 3px; font-size: 15px; color: var(--ink-soft); }

  .contact { margin-top: 18px; font-size: 12.5px; line-height: 1.55; color: var(--ink-soft); }
  .contact__row { display: flex; align-items: center; gap: 8px; }
  .contact__icon { width: 11px; height: 11px; fill: var(--ink-soft); flex: none; }
  .contact__address { padding-left: 19px; max-width: 320px; }

  .card--back .wordmark__square { background: var(--mark-light); }
  .card--back .wordmark__name { color: var(--mark-light); }
</style>
</head>
<body>
<main class="sheet">
  <section class="card card--front" aria-label="Business card front">
    <div class="wordmark">
      <span class="wordmark__square"></span>
      <span class="wordmark__name">Hollerby Whitlock Group</span>
    </div>
    <div class="wordmark-rule"></div>

    <div class="person">
      <h1 class="person__name">Daniel R. Whitlock</h1>
      <p class="person__title">Co-Founder &amp; Partner</p>
    </div>

    <div class="contact">
      <p class="contact__address">418 Bramblewood Ave. SE | Suite 2716 | Washington, D.C. 20019</p>
      <p class="contact__row">
        <svg class="contact__icon" viewBox="0 0 24 24" aria-hidden="true"><path d="M6.6 10.8a15.1 15.1 0 0 0 6.6 6.6l2.2-2.2c.3-.3.7-.4 1-.2 1.1.4 2.3.6 3.6.6.6 0 1 .4 1 1V20c0 .6-.4 1-1 1A17 17 0 0 1 3 4c0-.6.4-1 1-1h3.5c.6 0 1 .4 1 1 0 1.3.2 2.5.6 3.6.1.3 0 .7-.2 1z"/></svg>
        (202) 555-0187
      </p>
      <p class="contact__row">
        <svg class="contact__icon" viewBox="0 0 24 24" aria-hidden="true"><path d="M2 5h20v14H2z M2 5l10 8 10-8" fill="none" stroke="#6a6a6a" stroke-width="2"/></svg>
        Daniel@HollerbyWhitlock.com
      </p>
    </div>
  </section>

  <section class="card card--back" aria-label="Business card back">
    <div class="wordmark">
      <span class="wordmark__square"></span>
      <span class="wordmark__name">Hollerby Whitlock Group</span>
    </div>
  </section>
</main>
</body>
</html>
```